Job advertisement

A graphic job advertisement. It's supposed to be slightly different from the normal ads. Eye-catcher and later the text for the job description.

```html
<!DOCTYPE html>
<html lang="de">
<head>
<meta charset="utf-8">
<title>Stellenanzeige – Power-Worker gesucht</title>
<link rel="stylesheet" href="https://fonts.googleapis.com/css2?family=Didact+Gothic&family=Kumbh+Sans:wght@700&display=swap">
<style>
  :root {
    --ink: #000000;
    --glow-core: #f4e27a;
    --glow-mid: #b5822e;
    --glow-deep: #5a3414;
    --text: #ffffff;
    --ampere: #1a4cff;
    --ohm: #f03a35;
    --strom: #3fa535;
    --spannung: #e656ef;
    --volt: #ffffff;
    --leistung: #f0903a;
    --watt: #fff14a;
    --wire: #ff3a2e;
    --brand: #7e939b;
    --brand-dot: #e83a32;
  }
  * { margin: 0; padding: 0; box-sizing: border-box; }
  html, body { width: 1000px; height: 1200px; overflow: hidden; background: var(--ink); }
  .poster {
    position: relative;
    width: 1000px;
    height: 1200px;
    overflow: hidden;
    background: var(--ink);
    font-family: "Didact Gothic", sans-serif;
    color: var(--text);
  }
  .hero-art {
    position: absolute;
    inset: 0;
    background:
      radial-gradient(ellipse 90px 110px at 514px 560px, #ffffff 0%, rgba(255,255,255,0.85) 60%, rgba(255,255,255,0) 100%),
      radial-gradient(ellipse 330px 420px at 500px 600px, var(--glow-core) 0%, var(--glow-mid) 35%, var(--glow-deep) 65%, rgba(0,0,0,0) 100%);
  }
  .wires { position: absolute; inset: 0; }
  .wires polyline {
    fill: none;
    stroke: var(--wire);
    stroke-width: 2.4;
    stroke-linejoin: round;
    filter: drop-shadow(0 0 3px rgba(255,60,40,0.8));
  }
  .term { position: absolute; }
  .term-title {
    font-family: "Kumbh Sans", sans-serif;
    font-weight: 700;
    font-size: 40px;
    line-height: 40px;
    letter-spacing: 0.5px;
  }
  .term-text {
    margin-top: 10px;
    font-size: 22px;
    line-height: 28.3px;
  }
  .term.align-right { text-align: right; }
  .term-ampere   { left: 348px; top: 38px; }
  .term-ampere .term-title   { color: var(--ampere); }
  .term-ohm      { right: 195px; top: 74px; }
  .term-ohm .term-title      { color: var(--ohm); }
  .term-strom    { left: 108px; top: 166px; }
  .term-strom .term-title    { color: var(--strom); }
  .term-spannung { right: 63px; top: 328px; }
  .term-spannung .term-title { color: var(--spannung); }
  .term-volt     { left: 45px; top: 417px; }
  .term-volt .term-title     { color: var(--volt); }
  .term-leistung { right: 94px; top: 591px; }
  .term-leistung .term-title { color: var(--leistung); }
  .term-watt     { left: 96px; top: 668px; }
  .term-watt .term-title     { color: var(--watt); }

  .callout {
    position: absolute;
    left: 0;
    width: 1035px;
    top: 753px;
    text-align: center;
    font-size: 28px;
    line-height: 34px;
  }
  .brand {
    position: absolute;
    left: 0;
    width: 1035px;
    top: 960px;
    display: flex;
    flex-direction: column;
    align-items: center;
    gap: 22px;
  }
  .brand-dot {
    width: 70px;
    height: 70px;
    border-radius: 50%;
    background: var(--brand-dot);
  }
  .brand-name {
    font-family: "Didact Gothic", sans-serif;
    font-size: 54px;
    line-height: 60px;
    color: var(--brand);
  }
</style>
</head>
<body>
<main class="poster">
  <div class="hero-art" role="img" aria-label="Silhouette eines Kopfes im Profil mit einer leuchtenden Glühbirne im Inneren, warm hinterleuchtet"></div>

  <svg class="wires" width="1000" height="1200" viewBox="0 0 1000 1200" aria-hidden="true">
    <polyline points="521,57 546,57 520,521"/>
    <polyline points="697,95 645,95 539,526"/>
    <polyline points="257,184 293,184 502,529"/>
    <polyline points="700,346 679,346 551,549"/>
    <polyline points="160,435 335,435 493,551"/>
    <polyline points="717,610 677,610 550,571"/>
    <polyline points="222,690 380,690 490,576"/>
  </svg>

  <section class="term term-ampere">
    <h2 class="term-title">AMPERE</h2>
    <p class="term-text">Lorem ipsum<br>dolor sit amet,<br>consectetuer<br>adipiscing elit,<br>sed diam</p>
  </section>
  <section class="term term-ohm align-right">
    <h2 class="term-title">OHM</h2>
    <p class="term-text">Lorem ipsum<br>dolor sit amet,<br>consectetuer<br>adipiscing elit,<br>sed diam</p>
  </section>
  <section class="term term-strom">
    <h2 class="term-title">STROM</h2>
    <p class="term-text">Lorem ipsum<br>dolor sit amet,<br>consectetuer<br>adipiscing elit,<br>sed diam</p>
  </section>
  <section class="term term-spannung align-right">
    <h2 class="term-title">SPANNUNG</h2>
    <p class="term-text">Lorem ipsum<br>dolor sit amet,<br>consectetuer<br>adipiscing elit,<br>sed diam</p>
  </section>
  <section class="term term-volt">
    <h2 class="term-title">VOLT</h2>
    <p class="term-text">Lorem ipsum<br>dolor sit amet,<br>consectetuer<br>adipiscing elit,<br>sed diam</p>
  </section>
  <section class="term term-leistung align-right">
    <h2 class="term-title">LEISTUNG</h2>
    <p class="term-text">Lorem ipsum<br>dolor sit amet,<br>consectetuer<br>adipiscing elit,<br>sed diam</p>
  </section>
  <section class="term term-watt">
    <h2 class="term-title">WATT</h2>
    <p class="term-text">Lorem ipsum<br>dolor sit amet,<br>consectetuer<br>adipiscing elit,<br>sed diam</p>
  </section>

  <p class="callout">Wir suchen SIE !<br>Power-Worker<br>Bewerbung an :<br>personal@elektro-brandauer.de</p>

  <footer class="brand">
    <span class="brand-dot" aria-hidden="true"></span>
    <span class="brand-name">Elektro Brandauer</span>
  </footer>
</main>
</body>
</html>
```